Tarvel Plumbing Solutions

This is for my new plumbing company, I have attached an example of what I’m going for but want it to look better.

Target Market(s)

Home owners, real estate, etc.

Industry/Entity Type

Plumbing

Font styles to use
Other font styles liked:
• As per my logo and other examples uploaded

Colors

Designer to choose colors to be used in the design.

Requirements
Must have
• Must include my logo provided and similar to my flyer I have attached but better

```html
<!DOCTYPE html>
<html lang="en">
<head>
<meta charset="utf-8">
<title>Tarvel Plumbing Solutions – Flyer</title>
<link rel="stylesheet" href="https://fonts.googleapis.com/css2?family=Bebas+Neue&family=Roboto+Condensed:ital,wght@0,700;1,700&display=swap">
<style>
  :root{
    --page:#9a9a9a;
    --navy:#0a4aa6;
    --blue:#1f6fd0;
    --sky:#3d95ea;
    --pale:#cfe4fb;
    --ink:#0d0d12;
    --text:#16213a;
    --white:#ffffff;
  }
  *{margin:0;padding:0;box-sizing:border-box}
  html,body{width:858px;height:1200px;overflow:hidden;background:var(--page)}
  .flyer{
    position:absolute;left:71px;top:63px;width:716px;height:1073px;overflow:hidden;
    background:linear-gradient(160deg,#ffffff 0%,#e6f1fd 30%,#b9d8f7 70%,#9cc7f3 100%);
    font-family:"Roboto Condensed",sans-serif;
  }
  .shapes{position:absolute;inset:0}
  .headline{position:absolute;left:44px;font-family:"Bebas Neue",sans-serif;line-height:1;white-space:nowrap;transform-origin:left top}
  .headline--black{color:var(--ink)}
  .headline--navy{color:var(--navy)}
  .headline--sky{color:var(--sky)}

  .brand{position:absolute;left:480px;top:30px;width:210px;height:90px;display:flex;align-items:center;gap:10px;color:var(--white);font-weight:700}
  .brand__mark{width:46px;height:46px;border-radius:50%;border:3px solid var(--white);flex:none}
  .brand__name{line-height:1.02;font-size:25px;text-transform:uppercase}
  .brand__name small{display:block;font-size:14px;letter-spacing:.5px}

  .offer{position:absolute;left:487px;top:131px;width:196px;height:240px;border:1.5px solid var(--white);border-radius:26px;
    color:var(--white);text-align:center;font-weight:700;font-size:34px;line-height:44.5px;padding-top:10px}

  .service{position:absolute;left:93px;color:var(--text);font-weight:700;font-size:23px;line-height:29px;transform:translateY(-50%)}

  .section-title{position:absolute;left:278px;width:223px;text-align:center;color:var(--white);font-weight:700;font-size:56px;line-height:62px;top:756px}

  .contact{position:absolute;right:28px;text-align:right;white-space:nowrap;font-weight:700;transform:translateY(-50%)}
  .contact--phone{font-size:27px;color:var(--ink);letter-spacing:.3px}
  .contact--email{font-size:11.5px;font-style:italic;color:var(--ink)}
  .contact--social{font-size:13px;color:var(--ink)}
</style>
</head>
<body>
<main class="flyer">
  <svg class="shapes" width="716" height="1073" viewBox="0 0 716 1073">
    <defs>
      <linearGradient id="panelFill" x1="0" y1="0" x2="0" y2="1">
        <stop offset="0" stop-color="#0a4aa6"/>
        <stop offset="1" stop-color="#2a7ddc"/>
      </linearGradient>
      <linearGradient id="workerFill" x1="0" y1="0" x2="1" y2="1">
        <stop offset="0" stop-color="#cfdcea"/>
        <stop offset=".5" stop-color="#9aa7b5"/>
        <stop offset="1" stop-color="#e4e9ee"/>
      </linearGradient>
      <linearGradient id="fitterFill" x1="0" y1="0" x2="1" y2="0">
        <stop offset="0" stop-color="#b9d2ee" stop-opacity=".4"/>
        <stop offset="1" stop-color="#8fb4df"/>
      </linearGradient>
      <clipPath id="photoClip"><circle cx="478" cy="554" r="161"/></clipPath>
    </defs>

    <!-- right brand panel -->
    <rect x="697" y="0" width="19" height="1073" fill="#ffffff"/>
    <path d="M474 0 H697 V470 Q697 600 620 690 L474 690 Z" fill="url(#panelFill)"/>

    <!-- lower right photo area -->
    <rect x="501" y="655" width="215" height="320" fill="url(#fitterFill)" role="img" aria-label="Photo of a plumber in a hard hat tightening a pipe with a wrench"/>

    <!-- central services column -->
    <path d="M278 1073 V640 Q278 560 340 520 L501 520 V1073 Z" fill="var(--navy)"/>

    <!-- photo circle -->
    <circle cx="478" cy="554" r="182" fill="#ffffff"/>
    <circle cx="478" cy="554" r="168" fill="none" stroke="var(--sky)" stroke-width="3"/>
    <rect x="317" y="393" width="322" height="322" fill="url(#workerFill)" clip-path="url(#photoClip)" role="img" aria-label="Photo of a plumber fixing pipes under a kitchen sink"/>

    <!-- service bands -->
    <g>
      <rect x="0" y="420" width="53" height="56" fill="var(--navy)"/><circle cx="53" cy="448" r="28" fill="var(--navy)"/>
      <rect x="0" y="494" width="53" height="56" fill="var(--sky)"/><circle cx="53" cy="522" r="28" fill="var(--sky)"/>
      <rect x="0" y="565" width="53" height="56" fill="var(--navy)"/><circle cx="53" cy="593" r="28" fill="var(--navy)"/>
      <rect x="0" y="634" width="53" height="56" fill="var(--sky)"/><circle cx="53" cy="662" r="28" fill="var(--sky)"/>
      <rect x="0" y="709" width="53" height="56" fill="var(--navy)"/><circle cx="53" cy="737" r="28" fill="var(--navy)"/>
      <rect x="0" y="781" width="53" height="56" fill="var(--sky)"/><circle cx="53" cy="809" r="28" fill="var(--sky)"/>
      <rect x="0" y="854" width="53" height="56" fill="var(--navy)"/><circle cx="53" cy="882" r="28" fill="var(--navy)"/>
      <rect x="0" y="928" width="53" height="56" fill="var(--sky)"/><circle cx="53" cy="956" r="28" fill="var(--sky)"/>
      <rect x="0" y="999" width="53" height="56" fill="var(--navy)"/><circle cx="53" cy="1027" r="28" fill="var(--navy)"/>
    </g>
    <g fill="none" stroke="#ffffff" stroke-width="1" stroke-dasharray="3 2">
      <circle cx="53" cy="448" r="22"/><circle cx="53" cy="522" r="22"/><circle cx="53" cy="593" r="22"/>
      <circle cx="53" cy="662" r="22"/><circle cx="53" cy="737" r="22"/><circle cx="53" cy="809" r="22"/>
      <circle cx="53" cy="882" r="22"/><circle cx="53" cy="956" r="22"/><circle cx="53" cy="1027" r="22"/>
    </g>
    <!-- service icons -->
    <g fill="none" stroke="#ffffff" stroke-width="2" stroke-linecap="round" stroke-linejoin="round">
      <path d="M44 440 q-3 8 6 17 q9 9 17 6 l-3 -5 l-5 2 q-6 -4 -10 -10 l2 -5 z"/>
      <circle cx="58" cy="444" r="7"/>
      <path d="M45 512 v20 M40 512 h10 M52 520 h12 v6"/><circle cx="45" cy="534" r="4"/>
      <path d="M42 587 h10 a8 8 0 0 1 0 12 h-10 z M60 590 v10 M56 603 q4 3 8 0 q4 3 8 0"/>
      <circle cx="50" cy="658" r="7"/><circle cx="58" cy="667" r="6"/><path d="M41 668 h10"/>
      <rect x="48" y="726" width="11" height="20" rx="2"/><path d="M53 731 v6 M44 731 v12"/>
      <path d="M38 809 h30 M53 798 v11 M53 815 l-2 4 a2 2 0 0 0 4 0 z"/>
      <circle cx="53" cy="880" r="10"/><path d="M43 880 h20 M53 870 v20 M44 890 q4 3 9 0 q5 3 9 0"/>
      <path d="M53 970 c-8 -10 -10 -14 -10 -18 a10 10 0 0 1 20 0 c0 4 -2 8 -10 18 z"/><rect x="48" y="948" width="10" height="7" rx="1"/>
      <circle cx="53" cy="1027" r="5"/><circle cx="53" cy="1027" r="11" stroke-dasharray="4 3" stroke-width="3"/>
    </g>

    <!-- social circle -->
    <circle cx="382" cy="1038" r="19" fill="none" stroke="#ffffff" stroke-width="2"/>

    <!-- contact icons -->
    <circle cx="710" cy="969" r="22" fill="var(--navy)"/>
    <path d="M704 962 q-2 6 4 12 q6 6 12 4 l-2 -4 l-4 1 q-4 -3 -6 -7 l1 -4 z" fill="none" stroke="#ffffff" stroke-width="1.6"/>
    <circle cx="710" cy="1012" r="20" fill="var(--navy)"/>
    <rect x="700" y="1006" width="16" height="11" fill="none" stroke="#ffffff" stroke-width="1.4"/>
    <path d="M700 1006 l8 6 l8 -6" fill="none" stroke="#ffffff" stroke-width="1.4"/>
    <circle cx="710" cy="1046" r="20" fill="var(--navy)"/>
  </svg>

  <div class="headline headline--black" style="top:42px;font-size:63px;transform:scaleX(.81)">YOUR LOCAL RELIABLE</div>
  <div class="headline headline--navy" style="top:116px;font-size:74px;transform:scaleX(.92)">SYDNEY PLUMBER</div>
  <div class="headline headline--black" style="top:211px;font-size:43px;transform:scaleX(.76)">SPECIALISING IN ALL ASPECTS OF</div>
  <div class="headline headline--sky" style="top:262px;font-size:59px;transform:scaleX(.82)">PLUMBING, DRAINAGE &amp;</div>
  <div class="headline headline--navy" style="top:331px;font-size:69px;transform:scaleX(.87)">GAS MAINTENANCE.</div>

  <div class="brand">
    <span class="brand__mark"></span>
    <span class="brand__name">Tarvel<small>Plumbing Solutions</small></span>
  </div>

  <div class="offer">Mention<br>this flyer<br>to receive<br>15%<br>DISCOUNT</div>

  <div class="service" style="top:448px">Emergency<br>Plumbing</div>
  <div class="service" style="top:522px">Plumbing<br>Maintenance</div>
  <div class="service" style="top:593px">Drainage<br>Maintenance</div>
  <div class="service" style="top:662px">Gas<br>Maintenance</div>
  <div class="service" style="top:737px">Hot water<br>Systems</div>
  <div class="service" style="top:809px">Leaking Fixtures</div>
  <div class="service" style="top:882px">Blocked Sewer &amp;<br>Stormwater</div>
  <div class="service" style="top:956px">Camera &amp;<br>Locating</div>
  <div class="service" style="top:1027px">TMV<br>Maintenance</div>

  <div class="section-title">Our<br>Services</div>

  <div class="contact contact--phone" style="top:969px">0400 316 729</div>
  <div class="contact contact--email" style="top:1012px">hello@tarvelplumbing.com.au</div>
  <div class="contact contact--social" style="top:1046px">@Tarvel PlumbingSolutions</div>
</main>
</body>
</html>
```